Cardboard hanging box designs

I need to get some cardboard boxes made up for trailer wheel bearing kits. They need to be hanging boxes as pictured. The box needs to fit with our existing colour scheme and be clearly evident that it is for trailers. I am after 2 designs, one for "Trailer Bearing Kit" and one for "Marine Bearing Kit".
The Marine Bearing kit box should measure, 180mm High, 120mm Wide, 60mm Deep.
The Trailer Bearing kit box should measure, 180mm high, 120mm Wide, 30mm Deep.
These are all external measurements.

```html
<!DOCTYPE html>
<html lang="en">
<head>
<meta charset="utf-8">
<title>KVR Parts – Trailer Bearing Kit hanging box</title>
<link rel="stylesheet" href="https://fonts.googleapis.com/css2?family=Montserrat:wght@700;800;900&family=Oswald:wght@500;700&display=swap">
<style>
  :root {
    --page: #ffffff;
    --tab-yellow: #dccb35;
    --face-yellow: #e3c832;
    --side-yellow: #f2e03e;
    --brand-red: #a01c25;
    --brand-red-deep: #8c1720;
    --side-red: #e0242c;
    --panel-grey: #e6e6e6;
    --panel-grey-light: #f6f6f6;
    --ink: #111111;
    --white: #ffffff;
  }
  * { box-sizing: border-box; margin: 0; padding: 0; }
  html, body {
    width: 835px;
    height: 1200px;
    overflow: hidden;
    background: var(--page);
    font-family: "Montserrat", sans-serif;
  }
  .canvas {
    position: relative;
    width: 835px;
    height: 1200px;
  }

  /* ---------- side panel ---------- */
  .side-panel {
    position: absolute;
    left: 82px;
    top: 280px;
    width: 130px;
    height: 840px;
    background: var(--side-yellow);
    text-align: center;
  }
  .side-brand {
    position: absolute;
    left: 0;
    right: 0;
    top: 60px;
    height: 400px;
    display: flex;
    justify-content: center;
    align-items: center;
  }
  .side-brand-text {
    writing-mode: vertical-rl;
    transform: rotate(180deg);
    color: var(--ink);
    font-family: "Montserrat", sans-serif;
    font-weight: 900;
    line-height: 0.95;
    white-space: nowrap;
  }
  .side-brand-text .brand-main {
    display: block;
    font-size: 84px;
    letter-spacing: -1px;
  }
  .side-brand-text .brand-sub {
    display: block;
    font-size: 26px;
    letter-spacing: 16px;
  }
  .side-copy {
    position: absolute;
    left: 10px;
    right: 10px;
    top: 515px;
    font-family: "Oswald", sans-serif;
  }
  .side-fit {
    color: var(--side-red);
    font-weight: 500;
    font-size: 18px;
    line-height: 1.3;
  }
  .side-rule {
    height: 3px;
    background: var(--side-red);
    margin: 12px 0;
  }
  .side-title {
    color: var(--ink);
    font-weight: 700;
    font-size: 34px;
    line-height: 1.05;
  }
  .side-type {
    color: var(--side-red);
    font-weight: 500;
    font-size: 16px;
    line-height: 1.3;
  }

  /* ---------- front face ---------- */
  .box-face {
    position: absolute;
    left: 212px;
    top: 80px;
    width: 540px;
    height: 1040px;
  }
  .hang-tab {
    position: absolute;
    left: 0;
    top: 0;
    width: 540px;
    height: 200px;
  }
  .front-panel {
    position: absolute;
    left: 0;
    top: 200px;
    width: 540px;
    height: 840px;
    overflow: hidden;
  }
  .panel-art {
    position: absolute;
    inset: 0;
  }
  .brand-name {
    position: absolute;
    left: 0;
    right: 0;
    top: 80px;
    text-align: center;
    color: var(--ink);
    font-weight: 900;
    line-height: 0.95;
  }
  .brand-name .brand-main {
    display: block;
    font-size: 118px;
    letter-spacing: -2px;
  }
  .brand-name .brand-sub {
    display: block;
    font-size: 40px;
    letter-spacing: 22px;
    padding-left: 22px;
  }
  .product-photo {
    position: absolute;
    left: 230px;
    top: 300px;
    width: 290px;
    height: 260px;
    border-radius: 40px;
    background: radial-gradient(ellipse at 45% 55%, #8d9296 0%, #5d6266 45%, #3a3d40 100%);
  }
  .product-copy {
    position: absolute;
    left: 36px;
    top: 590px;
    width: 400px;
  }
  .fit-note {
    color: var(--face-yellow);
    font-weight: 800;
    font-size: 24px;
    line-height: 1.25;
  }
  .rule {
    height: 3px;
    background: var(--face-yellow);
    margin: 10px 0 12px;
  }
  .product-title {
    color: var(--white);
    font-weight: 900;
    font-size: 50px;
    line-height: 1;
    letter-spacing: -0.5px;
  }
  .bearing-type {
    color: var(--face-yellow);
    font-weight: 800;
    font-size: 22px;
    line-height: 1.2;
  }
</style>
</head>
<body>
<main class="canvas">
  <aside class="side-panel">
    <div class="side-brand">
      <p class="side-brand-text">
        <span class="brand-main">KVR</span>
        <span class="brand-sub">PARTS</span>
      </p>
    </div>
    <div class="side-copy">
      <p class="side-fit">Fits 1-1/16”<br>Straight Spindle</p>
      <div class="side-rule"></div>
      <p class="side-title">TRAILER<br>BEARING<br>KIT</p>
      <div class="side-rule"></div>
      <p class="side-type">NORWOOD TYPE<br>BEARINGS</p>
    </div>
  </aside>

  <section class="box-face">
    <svg class="hang-tab" viewBox="0 0 540 200" aria-hidden="true">
      <rect x="0" y="0" width="540" height="200" fill="var(--tab-yellow)"/>
      <path d="M205 70 a14 14 0 0 1 26 -16 a24 24 0 0 1 32 0 a14 14 0 0 1 26 16 q20 14 20 40 q0 34 -30 34 h-64 q-30 0 -30 -34 q0 -26 20 -40 z"
            fill="var(--white)"/>
    </svg>

    <div class="front-panel">
      <svg class="panel-art" viewBox="0 0 540 840" preserveAspectRatio="none" aria-hidden="true">
        <defs>
          <radialGradient id="greyField" cx="55%" cy="30%" r="75%">
            <stop offset="0" stop-color="var(--panel-grey-light)"/>
            <stop offset="1" stop-color="var(--panel-grey)"/>
          </radialGradient>
        </defs>
        <rect x="0" y="0" width="540" height="840" fill="url(#greyField)"/>
        <path d="M0 190 C40 470 290 590 540 600 L540 840 L0 840 Z" fill="var(--face-yellow)"/>
        <path d="M0 240 C40 520 290 640 540 650 L540 840 L0 840 Z" fill="var(--brand-red)"/>
        <path d="M0 700 L540 660 L540 840 L0 840 Z" fill="var(--brand-red-deep)" opacity="0.35"/>
      </svg>

      <h1 class="brand-name">
        <span class="brand-main">KVR</span>
        <span class="brand-sub">PARTS</span>
      </h1>

      <div class="product-photo" role="img"
           aria-label="Photo of two tapered roller bearings, a grease seal and a split pin"></div>

      <div class="product-copy">
        <p class="fit-note">Fits 1-1/16”<br>Straight Spindle</p>
        <div class="rule"></div>
        <h2 class="product-title">TRAILER<br>BEARING KIT</h2>
        <div class="rule"></div>
        <p class="bearing-type">NORWOOD TYPE BEARINGS</p>
      </div>
    </div>
  </section>
</main>
</body>
</html>
```